Homepage web design

I need a homepage design that will be easy to build into a default Word Press theme. Basically, header, navigation, body with sidebar, and footer.

This website is for a small commercial real estate firm in the Washington DC, Maryland and Virginia market.

THIS IS NOT A HOUSING/RESIDENTIAL WEBSITE. PLEASE DO NOT ADD ANY PROPERTY SEARCH FUNCTIONALITY.

Target Market(s)

People looking for basic information about the team and services provided.

Industry/Entity Type

Real Estate

Requirements
Must have
• Professional look. Clean design.

```html
<!DOCTYPE html>
<html lang="en">
<head>
<meta charset="utf-8">
<title>KRB – Keystone Realty Brokerage</title>
<link href="https://fonts.googleapis.com/css2?family=Open+Sans:wght@400;600;700&display=swap" rel="stylesheet">
<style>
:root{
  --brand:#1f8a3c;
  --brand-light:#6cc04a;
  --ink:#333;
  --muted:#555;
  --nav:#a2a59b;
  --nav-line:#c9cbc4;
  --panel:#a9ac9f;
  --footer:#868a7e;
  --accent:#f4a23a;
  --arrow:#f08a10;
  --rule:#b5b5b5;
  --white:#fff;
}
*{box-sizing:border-box;margin:0;padding:0}
html,body{width:695px;height:1200px;overflow:hidden;background:var(--white)}
body{position:relative;font-family:"Open Sans",Arial,sans-serif;color:var(--ink)}
.abs{position:absolute}
.logo{left:11px;top:22px;color:var(--brand);font-weight:700;font-size:40px;line-height:40px;letter-spacing:1px}
.logo-tag{left:11px;top:64px;font-size:7px;font-weight:700;color:var(--ink);letter-spacing:.3px}
.search{left:514px;top:37px;width:140px;height:21px;border:1px solid #bbb;font-size:10px;color:#999;padding:3px 6px}
.search-btn{left:653px;top:37px;width:22px;height:22px;border-radius:50%;background:var(--brand-light)}
.nav{left:0;top:89px;width:695px;height:28px;background:var(--nav);border-bottom:2px solid var(--nav-line);display:flex}
.nav a{height:26px;line-height:26px;text-align:center;font-size:10px;font-weight:700;color:#333;text-decoration:none;text-transform:uppercase;border-right:1px solid var(--nav-line)}
.nav a:last-child{border-right:0}
.call{left:500px;top:126px;display:flex;align-items:center;gap:10px;font-size:12.5px;font-weight:600;color:#333}
.call-icon{width:23px;height:20px;border-radius:50%;background:var(--brand-light);display:flex;align-items:center;justify-content:center}
.slider{left:33px;top:152px;width:630px;height:315px;border:1px solid #ccc;box-shadow:0 0 2px #ccc}
.slide{position:absolute;left:8px;top:8px;width:614px;height:298px;background:linear-gradient(180deg,#9fc0de 0%,#c9d6de 40%,#8a8a84 75%,#5c5a50 100%)}
.dots{left:303px;top:483px;width:88px;height:24px;border-radius:12px;background:#aaa;display:flex;justify-content:center;align-items:center;gap:8px}
.dots span{width:11px;height:11px;border-radius:50%;background:#fff}
.dots span.on{background:#333}
.rule{left:33px;width:630px;border-top:1px dotted var(--rule)}
.h2{font-size:14px;font-weight:400;text-transform:uppercase;color:#333}
.welcome-img{left:33px;top:564px;width:239px;height:134px;background:linear-gradient(180deg,#c7d2d8 0%,#e9ecea 50%,#5aa7c9 75%,#7c7c72 100%)}
.welcome-text{left:287px;top:563px;width:376px;font-size:9.3px;line-height:12.4px;color:var(--muted)}
.welcome-text p+p{margin-top:10px}
.btn{left:287px;top:678px;width:73px;height:20px;border-radius:4px;background:#111;color:#fff;font-size:9.5px;font-weight:700;text-align:center;line-height:20px}
.services li{position:absolute;list-style:none;font-size:11px;color:#333;padding-left:16px}
.services li::before{content:"";position:absolute;left:0;top:2px;border-left:9px solid var(--arrow);border-top:5px solid transparent;border-bottom:5px solid transparent}
.divider{left:325px;top:743px;height:191px;border-left:1px dotted var(--rule)}
.post-img{left:351px;width:104px;height:74px;border:1px solid #999}
.post-title{left:464px;font-size:11px;color:#222}
.post-text{left:464px;width:200px;font-size:9.3px;line-height:12.4px;color:var(--muted)}
.post-meta{left:464px;display:flex;align-items:center;gap:4px;font-size:8.5px;color:#444}
.pill{border:1px solid #bbb;border-radius:2px;padding:0 3px;height:14px;line-height:12px;background:#eef0f4}
.carousel{left:33px;top:984px;width:630px;height:119px;background:var(--panel);border:1px solid #999}
.thumb{top:1002px;width:133px;height:88px;border:2px solid #fff}
.chev{top:1038px;border-top:7px solid transparent;border-bottom:7px solid transparent}
.orange{left:0;top:1136px;width:695px;border-top:2px solid var(--accent)}
.footer-links{left:8px;top:1143px;font-size:9.5px;color:#222;letter-spacing:.3px}
.footer-band{left:0;top:1166px;width:695px;height:34px;background:var(--footer);display:flex;align-items:center;justify-content:space-between;padding:0 8px}
.copy{font-size:9px;color:#fff}
.social{display:flex;gap:7px;padding-right:2px}
.social span{width:24px;height:24px;background:#f4f4f4;border-radius:2px}
</style>
</head>
<body>
<header>
  <div class="abs logo">KRB</div>
  <div class="abs logo-tag">KEYSTONE REALTY BROKERAGE</div>
  <div class="abs search">Search...</div>
  <div class="abs search-btn"></div>
  <nav class="abs nav">
    <a style="width:69px">Home</a><a style="width:114px">About Us</a><a style="width:112px">Contact Us</a><a style="width:92px">Blog</a><a style="width:93px">Services</a><a style="width:118px">Our Work</a><a style="width:97px">Client Login</a>
  </nav>
  <div class="abs call"><span class="call-icon"><svg width="12" height="12" viewBox="0 0 24 24"><path fill="#fff" d="M6.6 10.8a15 15 0 0 0 6.6 6.6l2.2-2.2c.3-.3.7-.4 1-.2 1.1.4 2.3.6 3.6.6.6 0 1 .4 1 1V20c0 .6-.4 1-1 1A17 17 0 0 1 3 4c0-.6.4-1 1-1h3.5c.6 0 1 .4 1 1 0 1.3.2 2.5.6 3.6.1.3 0 .7-.2 1z"/></svg></span>CALL US : 555 014 2270</div>
</header>

<main>
  <div class="abs slider"><div class="slide" role="img" aria-label="Modern two-storey glass house at dusk"></div></div>
  <div class="abs dots"><span class="on"></span><span></span><span></span><span></span></div>
  <div class="abs rule" style="top:524px"></div>

  <h2 class="abs h2" style="left:33px;top:536px">Welcome to KRB</h2>
  <div class="abs welcome-img" role="img" aria-label="White modern villa with swimming pool"></div>
  <div class="abs welcome-text">
    <p>Donec quam felis, ultricies nec, pellentesque eu, pretium quis, sem. Nulla consequat massa quis enim. Donec pede justo, fringilla vel, aliquet nec, vulputate eget, arcu. In enim justo, rhoncus ut, imperdiet a, venenatis vitae, justo. Nullam dictum felis eu pede mollis pretium. Lorem ipsum dolor sit amet, consectetuer adipiscing elit. Aenean commodo ligula eget dolor.</p>
    <p>Lorem ipsum dolor sit amet, consectetuer adipiscing elit. Aenean commodo ligula eget dolor. Aenean massa. Cum sociis natoque penatibus et magnis dis parturient montes, nascetur ridiculus mus.</p>
  </div>
  <div class="abs btn">READ MORE</div>
  <div class="abs rule" style="top:723px"></div>

  <h2 class="abs h2" style="left:33px;top:739px">Our Services</h2>
  <ul class="services">
    <li style="left:33px;top:767px">Fcena massa cum vbciosd</li>
    <li style="left:33px;top:796px">Ncina bbsa cum</li>
    <li style="left:33px;top:825px">Rceena tevsa bsm</li>
    <li style="left:33px;top:852px">Duis solicit</li>
    <li style="left:33px;top:881px">Bfis solicit</li>
    <li style="left:33px;top:910px">Qiss Pseicit</li>
    <li style="left:204px;top:767px">Suspdisse metus</li>
    <li style="left:204px;top:796px">Ygena tevsm</li>
    <li style="left:204px;top:825px">Rceena tevsa bsm</li>
    <li style="left:204px;top:852px">Duis solicit</li>
    <li style="left:204px;top:881px">Ncina bbsa cum</li>
  </ul>
  <div class="abs divider"></div>

  <h2 class="abs h2" style="left:351px;top:739px">Blog</h2>
  <div class="abs post-img" style="top:766px;background:linear-gradient(180deg,#a9c4de,#d8d2b8 55%,#6e8a4e)" role="img" aria-label="Yellow two-storey family house"></div>
  <div class="abs post-title" style="top:766px">Dsena massa cum vceena tevsa bsse.</div>
  <div class="abs post-text" style="top:786px">Arena massa cum vceena tevsa bsse &nbsp;metus massa cum vceena tevsa bsse &nbsp;metus.</div>
  <div class="abs post-meta" style="top:826px"><span class="pill">Like</span><span class="pill">3k</span><span class="pill" style="margin-left:6px">Share</span><span class="pill">316</span><span style="margin-left:4px">2 Aug 2013</span></div>

  <div class="abs post-img" style="top:860px;background:linear-gradient(180deg,#7fa8d6,#c8c4bc 55%,#7a8a5a)" role="img" aria-label="Two-storey house with stone facade"></div>
  <div class="abs post-title" style="top:858px">Cfna massa cum vceena tevsa bsse.</div>
  <div class="abs post-text" style="top:878px">Arena massa cum vceena tevsa bsse &nbsp;metus massa cum vceena tevsa bsse &nbsp;metus.</div>
  <div class="abs post-meta" style="top:918px"><span class="pill">Like</span><span class="pill">3k</span><span class="pill" style="margin-left:6px">Share</span><span class="pill">316</span><span style="margin-left:4px">2 Aug 2013</span></div>

  <h2 class="abs h2" style="left:33px;top:958px">Featured Work</h2>
  <div class="abs carousel"></div>
  <div class="abs chev" style="left:41px;border-right:9px solid #555"></div>
  <div class="abs chev" style="left:647px;border-left:9px solid #555"></div>
  <div class="abs thumb" style="left:63px;background:linear-gradient(180deg,#5a9ad8,#e8eef2 55%,#7a9a6a)" role="img" aria-label="White colonial house with columns"></div>
  <div class="abs thumb" style="left:208px;background:linear-gradient(180deg,#cfd8e2,#cdbfa6 55%,#8a8470)" role="img" aria-label="Beige stone townhouse"></div>
  <div class="abs thumb" style="left:354px;background:linear-gradient(180deg,#b8cfe6,#3e4e6c 55%,#6e8a5a)" role="img" aria-label="Blue Victorian-style house"></div>
  <div class="abs thumb" style="left:499px;background:linear-gradient(180deg,#4a8a3a,#d8c99a 55%,#5e8a3e)" role="img" aria-label="Cream house surrounded by trees"></div>
</main>

<footer>
  <div class="abs orange"></div>
  <div class="abs footer-links">Home &nbsp;|&nbsp; About Us &nbsp;|&nbsp; Contact Us &nbsp;|&nbsp; Blog &nbsp;|&nbsp; Services &nbsp;|&nbsp; Our Work &nbsp;|&nbsp; Client Login</div>
  <div class="abs footer-band">
    <span class="copy">Copyright © 2013 keystonerb.com</span>
    <div class="social"><span></span><span></span><span></span><span></span><span></span></div>
  </div>
</footer>
</body>
</html>
```